Redesign Login page

I want to redesign my login page to bring my 2 products closer together. I am only looking to redesign one login page, not 2.

For the logo, please make it solid and it can be black or white if helpful. I can also fine tune the logo if you get it close.

Coding

Coded - Design and coding required

Number of Pages Required

1 page

```html
<!DOCTYPE html>
<html lang="en">
<head>
<meta charset="utf-8">
<title>Sheldra – Log In</title>
<link href="https://fonts.googleapis.com/css2?family=Poppins:wght@400;500&display=swap" rel="stylesheet">
<style>
  :root {
    --bg-light: #f2f7f6;
    --bg-mint: #d6e9e5;
    --bg-mist: #e8f1ef;
    --ink: #2b2b2b;
    --ink-soft: #555a5a;
    --ink-muted: #6b6f6f;
    --field-border: #c9cdcd;
    --brand-dark: #123f3a;
    --check: #2f5a56;
    --button: #84bdc2;
    --card: #ffffff;
    --card-edge: #a9d0d1;
  }
  * { box-sizing: border-box; margin: 0; padding: 0; }
  html, body { width: 1200px; height: 853px; overflow: hidden; }
  body {
    position: relative;
    font-family: "Poppins", sans-serif;
    color: var(--ink);
    background: var(--bg-light);
  }
  .backdrop {
    position: absolute; inset: 0;
    border-radius: 24px;
    background:
      radial-gradient(ellipse 420px 260px at 620px 40px, var(--bg-mint), transparent 70%),
      radial-gradient(ellipse 220px 200px at 1010px 330px, var(--bg-mint), transparent 70%),
      linear-gradient(180deg, var(--bg-mist), var(--bg-light) 60%, var(--bg-mist));
  }
  .brand {
    position: absolute; left: 33px; top: 33px;
    display: flex; align-items: center; gap: 10px;
  }
  .brand-dot {
    width: 54px; height: 54px; border-radius: 50%;
    background: #fff;
    display: flex; align-items: center; justify-content: center;
    font-weight: 500; font-size: 14px; color: var(--brand-dark);
  }
  .login-card {
    position: absolute; left: 376px; top: 111px;
    width: 448px; height: 607px;
    background: var(--card);
    border-radius: 22px;
    border: 1px solid transparent;
    border-bottom-color: var(--card-edge);
    border-left-color: var(--card-edge);
    box-shadow: 10px 14px 24px rgba(120, 170, 170, 0.25);
  }
  .close { position: absolute; left: 411px; top: 27px; width: 14px; height: 14px; }
  .title { position: absolute; left: 32px; top: 68px; font-size: 27px; font-weight: 400; }
  .label { position: absolute; left: 32px; font-size: 14.5px; color: var(--ink-soft); }
  .field {
    position: absolute; left: 32px; width: 382px; height: 46px;
    border: 1px solid var(--field-border); border-radius: 9px; background: #fff;
  }
  .toggle {
    position: absolute; right: 40px; top: 233px;
    display: flex; align-items: center; gap: 8px;
    font-size: 15px; color: var(--ink-muted);
  }
  .btn-login {
    position: absolute; left: 32px; top: 331px; width: 382px; height: 46px;
    border: 0; border-radius: 23px; background: var(--button);
    color: #fff; font: 400 16px "Poppins", sans-serif;
  }
  .remember {
    position: absolute; left: 34px; top: 393px;
    display: flex; align-items: center; gap: 10px; font-size: 14px;
  }
  .checkbox {
    width: 15px; height: 15px; border-radius: 2px; background: var(--check);
    display: flex; align-items: center; justify-content: center;
  }
  .help { position: absolute; right: 34px; top: 393px; font-size: 14px; }
  .signup { position: absolute; left: 33px; top: 472px; font-size: 14px; color: var(--ink-soft); }
  .signup a { color: var(--ink); font-weight: 500; text-decoration: underline; }
  .captcha {
    position: absolute; left: 32px; top: 501px;
    font-size: 14px; line-height: 20px; color: var(--ink-muted);
  }
  .captcha a { color: var(--ink); text-decoration: none; }
</style>
</head>
<body>
  <div class="backdrop" role="img" aria-label="Soft mint watercolour world map background"></div>

  <div class="brand"><div class="brand-dot">Sheldra</div></div>

  <main class="login-card">
    <svg class="close" viewBox="0 0 14 14" aria-label="Close">
      <path d="M1 1 L13 13 M13 1 L1 13" stroke="#555" stroke-width="1.6" stroke-linecap="round"/>
    </svg>

    <h1 class="title">Log In</h1>

    <label class="label" style="top:134px">Email or phone number</label>
    <div class="field" style="top:159px"></div>

    <label class="label" style="top:233px">Password</label>
    <div class="toggle">
      <svg width="16" height="14" viewBox="0 0 16 14" aria-hidden="true">
        <path d="M1 7 C4 2 12 2 15 7 C12 12 4 12 1 7 Z" fill="none" stroke="#8a8e8e" stroke-width="1.5"/>
        <circle cx="8" cy="7" r="2.2" fill="#8a8e8e"/>
        <path d="M2 13 L14 1" stroke="#8a8e8e" stroke-width="1.6" stroke-linecap="round"/>
      </svg>
      <span>Hide</span>
    </div>
    <div class="field" style="top:258px"></div>

    <button class="btn-login">Log In</button>

    <div class="remember">
      <span class="checkbox">
        <svg width="11" height="9" viewBox="0 0 11 9" aria-hidden="true">
          <path d="M1 4.5 L4 7.5 L10 1" fill="none" stroke="#fff" stroke-width="1.7"/>
        </svg>
      </span>
      Remember me
    </div>
    <div class="help">Need help?</div>

    <p class="signup">Don’t have an acount? <a href="#">Sign up</a></p>
    <p class="captcha">This page is protected by Guardline Check<br>to ensure you're not a bot. <a href="#">Learn more.</a></p>
  </main>
</body>
</html>
```